Larkfield Claim Services Philosophy/Positioning Flyer

I want to create a one page promotional ad/flyer to describe a little about our viewpoint.
The idea is we focus on fundamentals, which are often viewed as the small steps. But we recognize today’s challenges, but hold value in what the adjusting process and the adjuster deliver; recognizing it impacts both a consumer concern and a carrier concern. It’s a small thing but we do it in a great way. We just want to be the best.

Target Market(s)

Insurance company vendor managers and claims personnel

Industry/Entity Type

Insurance

Requirements
Must have
• professional, clean design, good flow, something that sells quality
Nice to have
• good color blend
Should not have
• cartoon type graphics or photos

```html
<!DOCTYPE html>
<html lang="en">
<head>
<meta charset="utf-8">
<title>Larkfield Claim Services – Fundamentals Flyer</title>
<link rel="stylesheet" href="https://fonts.googleapis.com/css2?family=Lato:wght@400;700&family=Roboto+Condensed:wght@700&display=swap">
<style>
:root{
  --page:#e9e6e1;
  --paper:#ffffff;
  --blue:#1c7cc4;
  --navy:#2626a3;
  --dark:#4a4a4d;
  --ink:#1d1d1f;
  --badge:#b9b9bd;
}
*{margin:0;padding:0;box-sizing:border-box}
html,body{width:1200px;height:1200px;overflow:hidden;background:var(--page)}
.flyer{position:absolute;left:160px;top:30px;width:988px;height:1280px;background:var(--paper);
  transform:scale(.89);transform-origin:0 0;font-family:"Lato",sans-serif;color:var(--ink);overflow:hidden;
  box-shadow:0 6px 20px rgba(0,0,0,.18)}
.abs{position:absolute}
.brand-name{left:300px;top:58px;width:230px;font-weight:700;font-size:21px;color:var(--blue);line-height:1.15;text-align:center}
.badge{left:560px;top:32px;width:96px;height:92px;background:var(--badge);border-radius:6px}
.hero-photo{left:0;top:150px;width:988px;height:462px;
  background:linear-gradient(100deg,#9fb3c4 0%,#dfeaf2 35%,#e8f1f7 55%,#8eb0d6 80%,#6f97c9 100%)}
.shapes{left:0;top:0}
.headline{right:42px;top:630px;font-family:"Roboto Condensed",sans-serif;font-weight:700;font-size:31px;line-height:36px;color:#fff;text-align:right}
.tab{left:0;background:var(--blue);color:#fff;border-radius:0 16px 16px 0;box-shadow:0 6px 8px -4px rgba(0,0,0,.25)}
.tab-focus{top:664px;width:310px;height:62px;padding:8px 0 0 42px;font-size:20px;line-height:22px}
.tab-focus small{font-size:16px;display:block;line-height:22px}
.tab-challenge{top:998px;width:295px;height:34px;padding:5px 0 0 42px;font-size:19px;letter-spacing:.5px}
.fundamentals{left:40px;top:750px;width:335px;list-style:none}
.fundamentals li{display:flex;align-items:flex-start;gap:8px;font-weight:700;font-size:16px;line-height:19px;margin-bottom:21px}
.fundamentals li:nth-child(3){margin-bottom:19px}
.dot{flex:0 0 30px;height:30px;border-radius:50%;background:var(--blue);margin-top:-5px;display:flex;align-items:center;justify-content:center}
.challenge-text{left:41px;top:1048px;width:332px;font-size:15px;line-height:18.5px;text-align:justify}
.body-text{left:415px;top:754px;font-size:15px;line-height:18.5px;text-align:justify}
.body-wide{width:532px}
.body-narrow{width:243px}
.body-text p+p{margin-top:18px}
.cycle{left:690px;top:808px;width:260px;height:260px}
.cycle-label{position:absolute;color:#fff;font-size:12px;line-height:15px;text-align:center}
.cycle-core{position:absolute;left:88px;top:110px;width:84px;text-align:center;font-weight:700;font-size:15px;line-height:19px;color:var(--ink)}
.retention{left:718px;top:1110px;font-size:16px;font-weight:700}
.slogan{left:415px;top:1052px;font-family:"Roboto Condensed",sans-serif;font-weight:700;font-size:35px;line-height:41px;color:#3e3e40}
.tagline{left:415px;top:1152px;font-size:15px}
.footer-name{left:41px;top:1160px;color:#fff;font-weight:700;font-size:17px;letter-spacing:.3px}
.contact{color:#fff;font-size:16px;display:flex;align-items:center;gap:8px}
.url{left:530px;top:1218px;width:400px;text-align:center;color:#fff;font-size:15px;letter-spacing:3px}
</style>
</head>
<body>
<main class="flyer">
  <div class="abs brand-name">Larkfield Claim Services, Inc.</div>
  <div class="abs badge" role="img" aria-label="Industry recognition badge"></div>

  <div class="abs hero-photo" role="img" aria-label="Photo: two smiling clients meeting an adjuster across a table with documents"></div>

  <svg class="abs shapes" width="988" height="1280" viewBox="0 0 988 1280" aria-hidden="true">
    <path d="M0 612 H988 V722 H420 Q395 722 380 700 L355 650 Q340 622 310 622 H0 Z" fill="var(--dark)"/>
    <path d="M0 622 H310 Q340 622 355 650 L370 680 L0 680 Z" fill="#fff"/>
    <line x1="393" y1="730" x2="393" y2="1145" stroke="#ddd" stroke-width="1"/>
    <path d="M0 1148 H355 Q380 1148 392 1170 L410 1200 Q420 1216 446 1216 H988 V1280 H0 Z" fill="var(--blue)"/>
    <path d="M430 1208 H988 V1245 H470 Q445 1245 430 1208 Z" fill="var(--dark)"/>
  </svg>

  <h1 class="abs headline">They may seem small, but the ripple effect of<br>doing the basic things right is extraordinary</h1>

  <div class="abs tab tab-focus">At Larkfield Claim Services,<small>we Focus on the Fundamentals</small></div>

  <ul class="abs fundamentals">
    <li><span class="dot"><svg width="16" height="14" viewBox="0 0 16 14"><circle cx="8" cy="4" r="3" fill="#fff"/><path d="M2 14 Q8 4 14 14Z" fill="#fff"/></svg></span>Immediate contact with the policyholder</li>
    <li><span class="dot"><svg width="16" height="12" viewBox="0 0 16 12"><rect x="1" y="1" width="14" height="10" fill="none" stroke="#fff" stroke-width="1.6"/></svg></span>Prompt scoping of the loss</li>
    <li><span class="dot"><svg width="12" height="16" viewBox="0 0 12 16"><rect x="1" y="1" width="10" height="14" fill="none" stroke="#fff" stroke-width="1.5"/><path d="M3 5H9M3 8H9M3 11H9" stroke="#fff"/></svg></span>Expedient submission of an accurate estimate to the carrier</li>
    <li><span class="dot"><svg width="18" height="12" viewBox="0 0 18 12"><rect x="3" y="1" width="12" height="8" fill="none" stroke="#fff" stroke-width="1.5"/><path d="M0 11H18" stroke="#fff" stroke-width="1.5"/></svg></span>Responsive communication</li>
    <li><span class="dot"><svg width="12" height="16" viewBox="0 0 12 16"><rect x="1" y="1" width="10" height="14" fill="none" stroke="#fff" stroke-width="1.5"/><rect x="3" y="4" width="6" height="5" fill="#fff"/></svg></span>Thorough file documentation</li>
  </ul>

  <h2 class="abs tab tab-challenge">THE CHALLENGE TODAY</h2>
  <p class="abs challenge-text">meet the consumers’ ever-changing expectations and demands driven by advances in technology. But is new technology the answer? Is claim estimating a self-service insurance item?</p>

  <div class="abs body-text body-wide">While technology may produce some cost savings and improve the estimating process, the fundamental process of an adjuster meeting with the policyholder</div>
  <div class="abs body-text body-narrow" style="top:791px">
    <p>and doing a physical inspection is still the most reliable method for preparing an accurate estimate. And, accurate indemnification supports policyholder retention through rate stability… which is also a consumer concern.</p>
    <p>Besides, a smile, a handshake and doing business face to face will deliver a positive experience during a troubled time.</p>
  </div>

  <div class="abs cycle">
    <svg width="260" height="260" viewBox="-10 -10 260 260" aria-hidden="true">
      <defs>
        <marker id="head" viewBox="0 0 10 10" refX="1" refY="5" markerUnits="userSpaceOnUse" markerWidth="36" markerHeight="84" orient="auto" preserveAspectRatio="none">
          <path d="M0 0 L10 5 L0 10 Z" fill="var(--navy)"/>
        </marker>
      </defs>
      <g fill="none" stroke="var(--navy)" stroke-width="56" marker-end="url(#head)">
        <path d="M37.9 98 A85 85 0 0 1 149.1 40.1"/>
        <path d="M180.1 59.9 A85 85 0 0 1 174.6 185.1"/>
        <path d="M142 202.1 A85 85 0 0 1 36.3 134.8"/>
      </g>
    </svg>
    <span class="cycle-label" style="left:76px;top:26px;width:100px">Accurate<br>Indemnification</span>
    <span class="cycle-label" style="left:186px;top:120px;width:58px">Accurate<br>Valuation</span>
    <span class="cycle-label" style="left:32px;top:164px;width:58px">Accurate<br>Pricing</span>
    <span class="cycle-core">Rate<br>Stability</span>
  </div>
  <svg class="abs" style="left:774px;top:1068px" width="120" height="22" aria-hidden="true"><path d="M0 0H120L60 22Z" fill="var(--navy)"/></svg>
  <div class="abs retention">POLICYHOLDER RETENTION</div>

  <div class="abs slogan">Small things done<br>IN A GREAT WAY!</div>
  <p class="abs tagline">We may not be the only IA firm you use, we just want to be the best one you use.</p>

  <div class="abs footer-name">LARKFIELD CLAIM SERVICES, INC</div>
  <div class="abs contact" style="left:41px;top:1190px">
    <svg width="20" height="20" viewBox="0 0 20 20"><circle cx="10" cy="10" r="9" fill="none" stroke="#fff" stroke-width="1.5"/><path d="M7 5 Q5 10 9 14 Q11 16 13 15 L12 12 L10 12 Q8 10 9 8 L9 6Z" fill="#fff"/></svg>(555) 014-2270
  </div>
  <div class="abs contact" style="left:226px;top:1190px">
    <svg width="22" height="18" viewBox="0 0 22 18"><rect x="5" y="0" width="12" height="5" fill="#fff"/><rect x="0" y="5" width="22" height="8" rx="2" fill="#fff"/><rect x="5" y="11" width="12" height="7" fill="#fff" stroke="var(--blue)"/></svg>(555) 014-2291
  </div>
  <div class="abs contact" style="left:38px;top:1222px">
    <svg width="24" height="20" viewBox="0 0 24 20"><path d="M12 1 L23 11 H20 V19 H14 V13 H10 V19 H4 V11 H1 Z" fill="#fff"/></svg>1420 Alder Court #210, Westbrook, CA. 90000
  </div>
  <div class="abs url">www.larkfieldclaims.com</div>
</main>
</body>
</html>
```